Young a vibrant Letting agent. New approach to the old market. our colors are various shades of green. We want a clean and clear design with our logo and beautiful shapes. Not too crowded but not too empty. Surprise us!

Size A5, (A4 folded in two)-Cover-Page2-Page3-Back Cover

Once the first and last page is designed, i will send you the content for page 2 and 3

```html
<!DOCTYPE html>
<html lang="en">
<head>
<meta charset="utf-8">
<title>Verdale Lettings – Brochure</title>
<link rel="stylesheet" href="https://fonts.googleapis.com/css2?family=Open+Sans:ital,wght@0,400;0,600;0,700;0,800;1,600;1,700&display=swap">
<style>
:root{
  --ink:#111311;
  --black:#0c0d0c;
  --green:#2f7d2f;
  --green-bright:#3fae2a;
  --green-deep:#1d4f22;
  --green-soft:#7fa886;
  --silver-1:#ffffff;
  --silver-2:#d9dcdb;
  --silver-3:#b9bdbc;
  --text:#2c2f2d;
  --stage:#e7eae7;
}
*{box-sizing:border-box;margin:0;padding:0}
html,body{width:1200px;height:900px;overflow:hidden}
body{background:var(--stage);font-family:"Open Sans",Arial,sans-serif;color:var(--text);position:relative}

.sheet{position:absolute;left:300px;width:600px;height:424px;display:flex;box-shadow:0 2px 10px rgba(0,0,0,.18)}
.sheet--outer{top:18px}
.sheet--inner{top:458px}
.page{position:relative;width:300px;height:424px;overflow:hidden}
.page + .page{border-left:1px solid rgba(0,0,0,.12)}
.page__shapes{position:absolute;inset:0;width:300px;height:424px}

.silver{background:radial-gradient(ellipse at 55% 45%,var(--silver-1) 0%,var(--silver-2) 65%,var(--silver-3) 100%)}

.flourish{position:absolute;border-radius:50%;background:radial-gradient(ellipse,rgba(63,120,70,.45) 0%,rgba(63,120,70,0) 70%)}

/* brand mark */
.brand{position:absolute;display:flex;align-items:center;gap:5px;background:#fff;padding:6px 8px;border:1px solid #cfd3d1}
.brand__square{width:9px;height:9px;background:var(--green)}
.brand__name{font-weight:800;color:var(--green);font-size:13px;letter-spacing:.2px}

/* back cover */
.back-brand{left:78px;top:150px}
.contacts{position:absolute;left:0;right:0;top:250px;text-align:center;font-size:8.5px;color:#333;line-height:26px}

/* front cover */
.cover-title{position:absolute;left:14px;top:12px;color:#fff;font-style:italic;font-weight:600;font-size:14.5px}
.cover-photo{position:absolute;left:0;top:40px;width:300px;height:260px;background:linear-gradient(180deg,#e4e2dd 0%,#cfcac2 45%,#a59a8c 75%,#8a7a66 100%)}
.cover-brand{left:14px;top:350px;padding:5px 6px}
.cover-brand .brand__name{font-size:10px}
.cover-tagline{position:absolute;left:96px;right:12px;top:342px;color:#fff;font-style:italic;font-weight:600;font-size:9.2px;line-height:12px}

/* inner pages */
.ribbon{position:absolute;background:var(--black);color:#fff;font-weight:700;text-transform:uppercase;letter-spacing:.6px;padding:4px 20px 4px 12px;clip-path:polygon(0 0,100% 0,calc(100% - 9px) 50%,100% 100%,0 100%);font-size:10px}
.ribbon--why{left:6px;top:48px}
.ribbon--pm{left:152px;top:122px;font-size:8.5px;padding-right:16px}
.ribbon--fees{left:12px;top:34px;font-size:13px;padding:5px 26px 5px 12px}

.bullets{position:absolute;list-style:none;font-size:6.4px;line-height:8.6px;color:#3a3d3b}
.bullets li{position:relative;padding-left:10px;margin-bottom:9px}
.bullets li::before{content:"";position:absolute;left:0;top:1.5px;width:5px;height:5px;background:var(--ink)}
.bullets--why{left:10px;top:78px;width:140px}
.bullets--pm{left:156px;top:148px;width:134px}

.street-photo{position:absolute;left:162px;top:28px;width:126px;height:86px;border:3px solid #fff;box-shadow:0 1px 4px rgba(0,0,0,.3);background:linear-gradient(180deg,#8fb2d6 0%,#c9d6e2 40%,#9b5a43 60%,#6d5a4c 100%)}
.badge{position:absolute;left:190px;top:330px;width:44px;height:44px;border-radius:50%;background:radial-gradient(circle,#2f8e96 0%,#1b5a60 70%);border:3px solid #d9b24a}

/* fees table */
.fees{position:absolute;left:12px;top:66px;width:278px;border-collapse:collapse;font-size:6px}
.fees th,.fees td{border:1px solid #9ca09e;height:16.5px;text-align:center;padding:0 2px}
.fees .fees__label{text-align:left;font-weight:700;width:110px;color:#222;background:#f2f3f2;line-height:6.5px}
.fees .fees__label small{display:block;font-weight:400;font-size:4.6px}
.fees thead th{font-weight:700}
.fees .fees__level{background:var(--black);color:#fff;text-align:left;font-size:7px}
.fees .fees__plan{background:var(--green);color:#fff;font-size:6.6px}
.fees .fees__cost-head{background:var(--black);color:#fff;font-size:10px;text-align:left}
.fees .fees__cost{background:#e6e7e6;color:#111;font-weight:700;font-size:6.8px}
.tick{width:11px;height:11px;display:block;margin:0 auto}
</style>
</head>
<body>

<svg width="0" height="0" style="position:absolute" aria-hidden="true">
  <defs>
    <symbol id="tick" viewBox="0 0 20 20">
      <circle cx="10" cy="10" r="9.5" fill="#3fae2a"/>
      <path d="M5.5 10.5 L8.7 13.6 L14.6 6.8" fill="none" stroke="#fff" stroke-width="2.4" stroke-linecap="round" stroke-linejoin="round"/>
    </symbol>
  </defs>
</svg>

<!-- Outer sheet: back cover + front cover -->
<section class="sheet sheet--outer">
  <article class="page page--back silver">
    <svg class="page__shapes" viewBox="0 0 300 424" aria-hidden="true">
      <path d="M0 0 H300 V18 C190 22 70 40 0 100 Z" fill="#0c0d0c"/>
      <path d="M0 112 C70 50 190 30 300 28" fill="none" stroke="#fff" stroke-width="3"/>
      <path d="M0 424 V330 C60 392 190 404 300 384 V424 Z" fill="#0c0d0c"/>
      <path d="M0 318 C60 384 190 394 300 374" fill="none" stroke="#fff" stroke-width="3"/>
    </svg>
    <div class="flourish" style="left:40px;top:20px;width:220px;height:60px" role="img" aria-label="Green flourish ornament"></div>
    <div class="flourish" style="left:10px;top:300px;width:200px;height:70px" role="img" aria-label="Green flourish ornament"></div>
    <div class="brand back-brand"><span class="brand__square"></span><span class="brand__name">Verdale Lettings</span></div>
    <div class="contacts">
      <p>Milton Keynes: 01632 960418</p>
      <p>London: 020 7946 0321</p>
      <p>Email: lettings@verdalelettings.co.uk</p>
      <p>www.verdalelettings.co.uk</p>
    </div>
  </article>

  <article class="page page--front" style="background:#fff">
    <div class="cover-photo" role="img" aria-label="Photo of a bright modern living room with white sofas and a stone fireplace"></div>
    <svg class="page__shapes" viewBox="0 0 300 424" aria-hidden="true">
      <path d="M0 0 H300 V46 C220 62 110 56 0 78 Z" fill="#0c0d0c"/>
      <path d="M0 84 C110 62 220 68 300 52" fill="none" stroke="#fff" stroke-width="3.5"/>
      <path d="M0 300 C80 262 200 268 300 250 V424 H0 Z" fill="#0c0d0c"/>
      <path d="M0 292 C80 254 200 260 300 242" fill="none" stroke="#fff" stroke-width="3.5"/>
    </svg>
    <h1 class="cover-title">Considering letting your property?</h1>
    <div class="flourish" style="left:60px;top:300px;width:240px;height:50px" role="img" aria-label="Green flourish ornament"></div>
    <div class="brand cover-brand"><span class="brand__square"></span><span class="brand__name">Verdale<br>Lettings</span></div>
    <p class="cover-tagline">We can help find tenants quickly, secure the best rents possible and professionally manage your property for a low, fixed fee.</p>
  </article>
</section>

<!-- Inner sheet: page 2 + page 3 -->
<section class="sheet sheet--inner">
  <article class="page page--two silver">
    <svg class="page__shapes" viewBox="0 0 300 424" aria-hidden="true">
      <path d="M0 0 H300 V16 C200 22 80 22 0 44 Z" fill="#0c0d0c"/>
      <path d="M0 52 C80 30 200 30 300 24" fill="none" stroke="#fff" stroke-width="3"/>
      <path d="M0 424 V366 C80 400 200 404 300 392 V424 Z" fill="#0c0d0c"/>
      <path d="M0 358 C80 392 200 396 300 384" fill="none" stroke="#fff" stroke-width="3"/>
    </svg>
    <h2 class="ribbon ribbon--why">Why choose us</h2>
    <ul class="bullets bullets--why">
      <li>By choosing Verdale Lettings to market your property, you choose to save money.</li>
      <li>We, unlike other agents, work on a no let no fee basis, and do not charge for marketing your property. Instructing us to market your property would cost nothing and you would only pay a fixed fee not a percentage if the property is let by us. If you let it through other agent, you will not be charged.</li>
      <li>We will attend viewings 7 days from 8am until 9pm, as most tenants are working during the day and would find very convenient evening and weekends appointments. We will carefully choose a suitable tenant, do all referencing, credit checks and employment referencing.</li>
      <li>We would present you all information we have and it is your decision. Call us today for a FREE, no obligation valuation on 01632 960418</li>
    </ul>
    <div class="street-photo" role="img" aria-label="Photo of a red brick terrace street with a To Let sign"></div>
    <h2 class="ribbon ribbon--pm">Property management</h2>
    <ul class="bullets bullets--pm">
      <li>Our experienced Property Management department looks after over 300 properties on behalf of our clients, relieving clients from the constant responsibility of being a landlord.</li>
      <li>In fact, many of our corporate tenants prefer managed properties. Starting at £34.99/month, our CarePlus Packages are designed to cover all maintenance issues on a "all-inclusive" basis and save the landlord money and time.</li>
    </ul>
    <div class="badge" role="img" aria-label="Satisfaction guarantee seal"></div>
  </article>

  <article class="page page--three silver">
    <svg class="page__shapes" viewBox="0 0 300 424" aria-hidden="true">
      <path d="M0 0 H300 V40 C220 22 100 14 0 16 Z" fill="#0c0d0c"/>
      <path d="M0 24 C100 22 220 30 300 48" fill="none" stroke="#fff" stroke-width="3"/>
      <path d="M0 424 V392 C100 404 220 396 300 362 V424 Z" fill="#0c0d0c"/>
      <path d="M0 384 C100 396 220 388 300 354" fill="none" stroke="#fff" stroke-width="3"/>
    </svg>
    <h2 class="ribbon ribbon--fees">Fees structure</h2>
    <table class="fees">
      <thead>
        <tr>
          <th class="fees__level">Level of Service</th>
          <th class="fees__plan">Letting only</th>
          <th class="fees__plan">CarePlus1</th>
          <th class="fees__plan">CarePlus2</th>
          <th class="fees__plan">CarePlus3</th>
        </tr>
        <tr>
          <th class="fees__cost-head">Cost</th>
          <th class="fees__cost">one off £250.00</th>
          <th class="fees__cost">£34.99/mo</th>
          <th class="fees__cost">£49.99/mo</th>
          <th class="fees__cost">£64.99/mo</th>
        </tr>
      </thead>
      <tbody>
        <tr><td class="fees__label">Comprehensive Marketing / Advertising</td><td><svg class="tick"><use href="#tick"/></svg></td><td><svg class="tick"><use href="#tick"/></svg></td><td><svg class="tick"><use href="#tick"/></svg></td><td><svg class="tick"><use href="#tick"/></svg></td></tr>
        <tr><td class="fees__label">Finding a tenant</td><td><svg class="tick"><use href="#tick"/></svg></td><td><svg class="tick"><use href="#tick"/></svg></td><td><svg class="tick"><use href="#tick"/></svg></td><td><svg class="tick"><use href="#tick"/></svg></td></tr>
        <tr><td class="fees__label">Obtaining references</td><td><svg class="tick"><use href="#tick"/></svg></td><td><svg class="tick"><use href="#tick"/></svg></td><td><svg class="tick"><use href="#tick"/></svg></td><td><svg class="tick"><use href="#tick"/></svg></td></tr>
        <tr><td class="fees__label">Drawing up tenancy agreements</td><td><svg class="tick"><use href="#tick"/></svg></td><td><svg class="tick"><use href="#tick"/></svg></td><td><svg class="tick"><use href="#tick"/></svg></td><td><svg class="tick"><use href="#tick"/></svg></td></tr>
        <tr><td class="fees__label">Checking in tenants</td><td><svg class="tick"><use href="#tick"/></svg></td><td><svg class="tick"><use href="#tick"/></svg></td><td><svg class="tick"><use href="#tick"/></svg></td><td><svg class="tick"><use href="#tick"/></svg></td></tr>
        <tr><td class="fees__label">Collecting and registering the deposit</td><td><svg class="tick"><use href="#tick"/></svg></td><td><svg class="tick"><use href="#tick"/></svg></td><td><svg class="tick"><use href="#tick"/></svg></td><td><svg class="tick"><use href="#tick"/></svg></td></tr>
        <tr><td class="fees__label">Organising the Gas Safety Inspection</td><td></td><td><svg class="tick"><use href="#tick"/></svg></td><td><svg class="tick"><use href="#tick"/></svg></td><td><svg class="tick"><use href="#tick"/></svg></td></tr>
        <tr><td class="fees__label">Organising the Mid-term Inspection</td><td></td><td><svg class="tick"><use href="#tick"/></svg></td><td><svg class="tick"><use href="#tick"/></svg></td><td><svg class="tick"><use href="#tick"/></svg></td></tr>
        <tr><td class="fees__label">Inventory Report</td><td></td><td><svg class="tick"><use href="#tick"/></svg></td><td><svg class="tick"><use href="#tick"/></svg></td><td><svg class="tick"><use href="#tick"/></svg></td></tr>
        <tr><td class="fees__label">24/7 Tenant On Call Service</td><td></td><td><svg class="tick"><use href="#tick"/></svg></td><td><svg class="tick"><use href="#tick"/></svg></td><td><svg class="tick"><use href="#tick"/></svg></td></tr>
        <tr><td class="fees__label">Organising Repairs &amp; Service</td><td></td><td></td><td><svg class="tick"><use href="#tick"/></svg></td><td><svg class="tick"><use href="#tick"/></svg></td></tr>
        <tr><td class="fees__label">Rent Collection</td><td></td><td></td><td><svg class="tick"><use href="#tick"/></svg></td><td><svg class="tick"><use href="#tick"/></svg></td></tr>
        <tr><td class="fees__label">Boiler Care and Repair<small>(all parts and labour included)</small></td><td></td><td></td><td></td><td><svg class="tick"><use href="#tick"/></svg></td></tr>
        <tr><td class="fees__label">Plumbing Repairs<small>(all parts and labour included)</small></td><td></td><td></td><td></td><td><svg class="tick"><use href="#tick"/></svg></td></tr>
        <tr><td class="fees__label">Electrical Repairs<small>(all parts and labour included)</small></td><td></td><td></td><td></td><td><svg class="tick"><use href="#tick"/></svg></td></tr>
      </tbody>
    </table>
  </article>
</section>

</body>
</html>
```